Holvern Incorporated

Holvern is a business that provides consulting, and manages and supplies trades persons in the construction and heavy industries sector. We build, do maintenance, install machinery, and can manage projects or jobs. Would like or prefer more clean, classic designs. Blacks/greys, but open to almost anything.

Target Market(s)

Industrial/Construction/Manufacturing

Industry/Entity Type

Construction Company

Contact Information for Business Card

Clean, business name on the front, possibly have the details on the back, but open to any ideas.

Logo Text

We currently do not have a slogan, open to ideas

Font styles to use
Serif
Sans Serif

Colors

Designer to choose colors to be used in the design.

Requirements
Should not have
• the oval is not my logo, was just an idea. please don't send 20 designs with the oval

```html
<!DOCTYPE html>
<html lang="en">
<head>
<meta charset="utf-8">
<title>Holvern Incorporated – Business Card</title>
<link href="https://fonts.googleapis.com/css2?family=Lato:wght@400;700&display=swap" rel="stylesheet">
<style>
  :root {
    --stage: #3a3a3a;
    --card-dark: #232425;
    --card-light: #ffffff;
    --swoosh-grey: #bdbdbd;
    --ink-dark: #2a2a2a;
    --ink-muted: #555555;
    --ink-light: #f2f2f2;
  }
  * { margin: 0; padding: 0; box-sizing: border-box; }
  html, body {
    width: 1200px; height: 900px; overflow: hidden;
    background: var(--stage);
    font-family: "Lato", sans-serif;
  }
  .stage {
    position: relative; width: 1200px; height: 900px;
    display: flex; align-items: center; justify-content: center; gap: 50px;
  }
  .card {
    position: relative; width: 525px; height: 300px;
    overflow: hidden; box-shadow: 0 14px 30px rgba(0,0,0,.45);
  }
  .card-front { background: var(--card-light); }
  .card-back { background: var(--card-dark); }
  .card-art { position: absolute; inset: 0; width: 100%; height: 100%; }

  .brand {
    position: absolute; display: flex; align-items: center; gap: 10px;
    font-weight: 700; letter-spacing: .5px; white-space: nowrap;
  }
  .brand-dot { width: 12px; height: 12px; border-radius: 50%; }
  .card-front .brand { top: 28px; right: 40px; font-size: 24px; color: var(--ink-dark); }
  .card-front .brand-dot { background: var(--ink-dark); }
  .card-back .brand { top: 110px; left: 50%; transform: translateX(-50%); font-size: 34px; color: var(--ink-light); }
  .card-back .brand-dot { background: var(--ink-light); }

  .holder { position: absolute; top: 40px; left: 34px; }
  .holder-name { font-size: 17px; font-weight: 700; color: var(--ink-dark); }
  .holder-title { font-size: 12px; color: var(--ink-muted); margin-top: 2px; }

  .contact {
    position: absolute; right: 36px; bottom: 20px;
    color: var(--ink-light); font-size: 13px; line-height: 1.35;
  }
  .contact-address { margin-bottom: 4px; }
  .contact-row { display: flex; align-items: center; gap: 8px; }
  .contact-icon { width: 11px; height: 11px; flex: none; }
  .contact-icon.blank { visibility: hidden; }

  .back-web {
    position: absolute; bottom: 40px; left: 0; right: 0; text-align: center;
    color: var(--ink-light); font-size: 14px; letter-spacing: .3px;
  }
</style>
</head>
<body>
<main class="stage">
  <section class="card card-front" aria-label="Card front">
    <svg class="card-art" viewBox="0 0 525 300" preserveAspectRatio="none" aria-hidden="true">
      <path d="M0,86 C150,86 230,140 525,98 L525,112 C250,154 150,102 0,100 Z" fill="var(--swoosh-grey)"/>
      <path d="M0,110 C150,104 240,164 525,122 L525,300 L0,300 Z" fill="var(--card-dark)"/>
      <path d="M0,122 C160,114 260,178 525,138 L525,148 C260,184 150,128 0,134 Z" fill="var(--card-light)"/>
    </svg>
    <div class="brand"><span class="brand-dot"></span>Holvern Incorporated</div>
    <div class="holder">
      <p class="holder-name">Daniel Ashcombe</p>
      <p class="holder-title">Manager</p>
    </div>
    <div class="contact">
      <div class="contact-address">
        <div class="contact-row"><span class="contact-icon blank"></span>418 Corrin Lane</div>
        <div class="contact-row"><span class="contact-icon blank"></span>Houston, TX 77041</div>
      </div>
      <div class="contact-row">
        <svg class="contact-icon" viewBox="0 0 12 12"><path d="M2.5 1 L4.5 1 L5.2 3.5 L4 4.6 C4.6 6 6 7.4 7.4 8 L8.5 6.8 L11 7.5 L11 9.5 C11 10.4 10.3 11 9.5 11 C5 11 1 7 1 2.5 C1 1.7 1.6 1 2.5 1 Z" fill="currentColor"/></svg>
        512 004 2270
      </div>
      <div class="contact-row">
        <svg class="contact-icon" viewBox="0 0 12 12"><rect x="3" y="1" width="6" height="3" fill="currentColor"/><rect x="1" y="4.5" width="10" height="5" rx="1" fill="currentColor"/><rect x="3" y="8" width="6" height="3" fill="currentColor"/></svg>
        512 004 2271
      </div>
      <div class="contact-row">
        <svg class="contact-icon" viewBox="0 0 12 12"><rect x="1" y="2.5" width="10" height="7" fill="none" stroke="currentColor"/><path d="M1 2.5 L6 6.5 L11 2.5" fill="none" stroke="currentColor"/></svg>
        info@holvern.com
      </div>
      <div class="contact-row">
        <svg class="contact-icon" viewBox="0 0 12 12"><circle cx="6" cy="6" r="5" fill="none" stroke="currentColor"/><ellipse cx="6" cy="6" rx="2.2" ry="5" fill="none" stroke="currentColor"/><path d="M1 6 H11" stroke="currentColor"/></svg>
        www.holvern.com
      </div>
    </div>
  </section>

  <section class="card card-back" aria-label="Card back">
    <div class="brand"><span class="brand-dot"></span>Holvern Incorporated</div>
    <p class="back-web">www.holvern.com</p>
  </section>
</main>
</body>
</html>
```